Tovrelan Ltda

Logo design focused on: - Construction of civil works - Electrical services - Metal structures - Equipment rental Tomás Ibarra Leiva Manager tovrelan.ltda@brevomail.example 56 9 48215037 Quelitoco s / n, Sorimar, Valle Arenal

Building

Colors
33a6d7
0292cd
33b8a4
0555a3

```html
<!DOCTYPE html>
<html lang="en">
<head>
<meta charset="utf-8">
<title>Tovrelan Ltda – Business Cards</title>
<link rel="stylesheet" href="https://fonts.googleapis.com/css2?family=Montserrat:wght@500;600;700&family=Questrial&display=swap">
<style>
  :root {
    --sky: #33a6d7;
    --azure: #0292cd;
    --teal: #33b8a4;
    --navy: #0555a3;
    --band: #22b3c4;
    --stage: #111112;
    --card-dark: #1b1b1d;
    --card-light: #ffffff;
    --ink: #3a3a3a;
    --ghost: #ececee;
  }
  * { box-sizing: border-box; margin: 0; padding: 0; }
  html, body { width: 1200px; height: 1000px; overflow: hidden; }
  body {
    background: var(--stage);
    font-family: "Questrial", sans-serif;
    display: flex;
    align-items: center;
    justify-content: center;
    gap: 40px;
  }
  .card {
    position: relative;
    width: 520px;
    height: 300px;
    border-radius: 22px;
    overflow: hidden;
    box-shadow: 0 18px 40px rgba(0,0,0,.55);
  }

  /* Back side */
  .card--back { background: var(--card-dark); }
  .services {
    position: absolute;
    top: 38px;
    left: 44px;
    list-style: none;
    font-family: "Montserrat", sans-serif;
    font-weight: 600;
    font-size: 13px;
    letter-spacing: .04em;
    text-transform: uppercase;
    color: var(--sky);
    line-height: 1.75;
  }
  .services li::before {
    content: "";
    display: inline-block;
    width: 5px; height: 5px;
    border-radius: 50%;
    background: var(--azure);
    margin-right: 9px;
    vertical-align: middle;
  }
  .brand {
    position: absolute;
    display: flex;
    align-items: center;
    gap: 12px;
  }
  .brand__dot {
    width: 46px; height: 46px;
    border-radius: 50%;
    background: var(--azure);
  }
  .brand__name {
    font-family: "Montserrat", sans-serif;
    font-weight: 600;
    font-size: 30px;
    letter-spacing: .03em;
    color: var(--navy);
  }
  .card--back .brand { left: 140px; top: 190px; }
  .card--back .brand__name { color: var(--azure); }

  /* Front side */
  .card--front { background: var(--card-light); }
  .ghost-mark {
    position: absolute;
    right: -60px; top: 120px;
    width: 300px; height: 300px;
    border-radius: 50%;
    background: var(--ghost);
  }
  .band {
    position: absolute;
    left: 0; right: 0; bottom: 0;
    height: 22px;
    background: var(--band);
  }
  .card--front .brand { left: 40px; top: 34px; }
  .person { position: absolute; left: 40px; top: 118px; }
  .person__name {
    font-family: "Montserrat", sans-serif;
    font-weight: 700;
    font-size: 19px;
    letter-spacing: .04em;
    text-transform: uppercase;
    color: var(--navy);
  }
  .person__role { font-size: 14px; color: var(--ink); margin-top: 2px; }
  .contact { position: absolute; left: 40px; top: 180px; list-style: none; }
  .contact li {
    display: flex; align-items: center; gap: 8px;
    font-size: 13.5px; color: var(--ink); line-height: 1.6;
  }
  .contact svg { width: 13px; height: 13px; fill: var(--azure); flex: none; }
  .address {
    position: absolute;
    right: 40px; bottom: 46px;
    font-size: 15px;
    line-height: 1.4;
    color: var(--ink);
    text-align: left;
  }
</style>
</head>
<body>
  <section class="card card--back" aria-label="Card back">
    <ul class="services">
      <li>Construction of civil works</li>
      <li>Electrical services</li>
      <li>Metal structures</li>
      <li>Equipment rental</li>
    </ul>
    <div class="brand">
      <span class="brand__dot"></span>
      <span class="brand__name">Tovrelan Ltda</span>
    </div>
  </section>

  <section class="card card--front" aria-label="Card front">
    <div class="ghost-mark"></div>
    <div class="brand">
      <span class="brand__dot"></span>
      <span class="brand__name">Tovrelan Ltda</span>
    </div>
    <div class="person">
      <p class="person__name">Tomás Ibarra Leiva</p>
      <p class="person__role">Manager</p>
    </div>
    <ul class="contact">
      <li>
        <svg viewBox="0 0 16 16" aria-hidden="true"><path d="M1 3h14v10H1z M1 3l7 6 7-6" fill="none" stroke="#0292cd" stroke-width="1.6"/></svg>
        tovrelan.ltda@brevomail.example
      </li>
      <li>
        <svg viewBox="0 0 16 16" aria-hidden="true"><path d="M4 1l3 3-2 2c1 2 3 4 5 5l2-2 3 3-2 3C7 15 1 9 1 3z"/></svg>
        56 9 48215037
      </li>
    </ul>
    <p class="address">Quelitoco s / n, Sorimar<br>Valle Arenal</p>
    <div class="band"></div>
  </section>
</body>
</html>
```